4' x 8' Construction Project Sign, think of a very large business card

We need project signs for our construction sites, the sign will be mounted along the road so cars driving by can quickly read. the sign should be able to be read as cars drive by doing highway speed.

Think like your making a large business card

I would like to include "NOW HIRING" Superintendents, Project Managers, Pipe Foremen, Pipe Layers, and Equipment Operators

Description of services we provide should include

Civil Construction Services
Land Clearing
Excavation
Underground Utilities
Environmental Maintenance

The 2 objectives is to market to future clients and to recruit new employees

The sign will be mounted on posts at the entrance of our construction projects
Updates

Low design quality

Target Market(s)

Construction and land developers

Industry/Entity Type

Construction Company

Other font styles liked:
• Hypatia Sans Pro lite

Colors

Designer to choose colors to be used in the design.

Requirements
Must have
• Clean and easy to read
• Civil Construction Services
• Land Clearing
• Excavation
• Underground Utilities
• Road Construction

```html
<!DOCTYPE html>
<html lang="en">
<head>
<meta charset="utf-8">
<title>Harlow Brothers – Project Sign Options</title>
<link rel="stylesheet" href="https://fonts.googleapis.com/css2?family=Catamaran:wght@600;700;800&family=Mulish:wght@700;800;900&display=swap">
<style>
  :root {
    --brand-blue: #1f3f7f;
    --frame-gray: #555659;
    --text-gray: #4a4b4e;
    --lavender: #7f83b8;
    --white: #ffffff;
  }
  * { box-sizing: border-box; margin: 0; padding: 0; }
  html, body {
    width: 1200px; height: 601px; overflow: hidden;
    background: var(--white);
  }
  .board { position: relative; width: 1200px; height: 601px; }

  .sign {
    position: absolute;
    width: 578px; height: 289px;
  }
  .sign--a { left: 0;     top: 0; }
  .sign--b { left: 622px; top: 0; }
  .sign--c { left: 0;     top: 312px; }
  .sign--d { left: 622px; top: 312px; }

  .sign__art { position: absolute; inset: 0; width: 578px; height: 289px; }

  .brand {
    position: absolute; left: 28px; top: 27px;
    display: flex; align-items: center; gap: 8px;
  }
  .brand__square {
    width: 48px; height: 48px;
    border: 6px solid var(--brand-blue);
  }
  .brand__rule { width: 1px; height: 50px; background: var(--frame-gray); }
  .brand__name {
    font-family: "Catamaran", sans-serif; font-weight: 700;
    color: var(--brand-blue); line-height: 1; white-space: nowrap;
    width: 212px;
  }
  .brand__line1 { display: block; font-size: 22.5px; letter-spacing: -0.2px; }
  .brand__line2 { display: block; font-size: 13.5px; letter-spacing: 3.6px; margin-top: 4px; }

  .services {
    position: absolute; left: 17px; width: 290px; top: 92px;
    list-style: none; text-align: center;
    font-family: "Catamaran", sans-serif; font-weight: 700;
    font-size: 15px; color: var(--text-gray);
  }
  .services li { height: 30px; line-height: 20px; white-space: nowrap; }

  .hiring {
    position: absolute; left: 360px; width: 192px; top: 28px;
    text-align: center; font-family: "Mulish", sans-serif;
  }
  .hiring__mark {
    width: 57px; height: 57px; margin: 0 auto;
    border: 3px solid var(--brand-blue);
    outline: 2px solid var(--brand-blue); outline-offset: -9px;
  }
  .hiring__title {
    margin-top: 20px;
    font-size: 27px; font-weight: 900; letter-spacing: 1.5px;
    color: var(--brand-blue); white-space: nowrap; line-height: 1;
  }
  .jobs { list-style: none; margin-top: 12px; }
  .jobs li {
    height: 25.8px; line-height: 20px;
    font-size: 13px; font-weight: 800; letter-spacing: 2.2px;
    color: var(--text-gray); white-space: nowrap;
  }

  .sign--c .hiring, .sign--d .hiring { left: 364px; top: 27px; }
  .sign--c .hiring__mark, .sign--d .hiring__mark {
    border-color: var(--white); outline-color: var(--white);
  }
  .sign--c .hiring__title, .sign--c .jobs li,
  .sign--d .hiring__title, .sign--d .jobs li { color: var(--white); }
</style>
</head>
<body>
<main class="board">

  <section class="sign sign--a">
    <svg class="sign__art" viewBox="0 0 578 289" aria-hidden="true">
      <defs>
        <linearGradient id="ribbonGray" x1="0" y1="0" x2="0" y2="1">
          <stop offset="0" stop-color="#1f3f7f"/>
          <stop offset="0.45" stop-color="#555659"/>
          <stop offset="1" stop-color="#ffffff"/>
        </linearGradient>
      </defs>
      <rect width="578" height="289" fill="#1f3f7f"/>
      <rect x="6" y="6" width="566" height="277" fill="#fff"/>
      <rect x="9" y="9" width="560" height="271" fill="#555659"/>
      <rect x="13" y="13" width="552" height="263" fill="#fff"/>
      <path d="M340 13 C356 60 358 110 343 160 C328 205 320 240 328 276 L314 276 C303 240 308 200 320 160 C333 120 336 60 316 13 Z" fill="url(#ribbonGray)"/>
    </svg>
    <div class="brand">
      <span class="brand__square"></span><span class="brand__rule"></span>
      <p class="brand__name"><span class="brand__line1">HARLOW BROTHERS</span><span class="brand__line2">CIVIL CONSTRUCTION</span></p>
    </div>
    <ul class="services">
      <li>- CIVIL CONSTRUCTION SERVICES -</li><li>- LAND CLEARING -</li><li>- EXCAVATION -</li>
      <li>- UNDERGROUND UTILITIES -</li><li>- ENVIRONMENTAL MAINTENANCE -</li><li>- ROAD CONSTRUCTION -</li>
    </ul>
    <div class="hiring">
      <div class="hiring__mark"></div>
      <h2 class="hiring__title">NOW HIRING!</h2>
      <ul class="jobs"><li>SUPERINTENDENTS</li><li>PROJECT MANAGERS</li><li>PIPE FOREMEN</li><li>PIPE LAWYERS</li><li>EQUIPMENT OPERATORS</li></ul>
    </div>
  </section>

  <section class="sign sign--b">
    <svg class="sign__art" viewBox="0 0 578 289" aria-hidden="true">
      <defs>
        <linearGradient id="ribbonLav" x1="0" y1="0" x2="0" y2="1">
          <stop offset="0" stop-color="#1f3f7f"/>
          <stop offset="0.5" stop-color="#7f83b8"/>
          <stop offset="1" stop-color="#ffffff"/>
        </linearGradient>
      </defs>
      <rect width="578" height="289" fill="#1f3f7f"/>
      <rect x="6" y="6" width="566" height="277" fill="#fff"/>
      <rect x="9" y="9" width="560" height="271" fill="#555659"/>
      <rect x="13" y="13" width="552" height="263" fill="#fff"/>
      <path d="M340 13 C356 60 358 110 343 160 C328 205 320 240 328 276 L314 276 C303 240 308 200 320 160 C333 120 336 60 316 13 Z" fill="url(#ribbonLav)"/>
    </svg>
    <div class="brand">
      <span class="brand__square"></span><span class="brand__rule"></span>
      <p class="brand__name"><span class="brand__line1">HARLOW BROTHERS</span><span class="brand__line2">CIVIL CONSTRUCTION</span></p>
    </div>
    <ul class="services">
      <li>- CIVIL CONSTRUCTION SERVICES -</li><li>- LAND CLEARING -</li><li>- EXCAVATION -</li>
      <li>- UNDERGROUND UTILITIES -</li><li>- ENVIRONMENTAL MAINTENANCE -</li><li>- ROAD CONSTRUCTION -</li>
    </ul>
    <div class="hiring">
      <div class="hiring__mark"></div>
      <h2 class="hiring__title">NOW HIRING!</h2>
      <ul class="jobs"><li>SUPERINTENDENTS</li><li>PROJECT MANAGERS</li><li>PIPE FOREMEN</li><li>PIPE LAWYERS</li><li>EQUIPMENT OPERATORS</li></ul>
    </div>
  </section>

  <section class="sign sign--c">
    <svg class="sign__art" viewBox="0 0 578 289" aria-hidden="true">
      <defs>
        <linearGradient id="shadowGray" x1="0" y1="0" x2="0" y2="1">
          <stop offset="0" stop-color="#ffffff"/>
          <stop offset="0.35" stop-color="#555659"/>
          <stop offset="0.7" stop-color="#555659"/>
          <stop offset="1" stop-color="#ffffff"/>
        </linearGradient>
      </defs>
      <rect width="578" height="289" fill="#1f3f7f"/>
      <rect x="6" y="6" width="566" height="277" fill="#fff"/>
      <rect x="9" y="9" width="560" height="271" fill="#555659"/>
      <rect x="13" y="13" width="552" height="263" fill="#fff"/>
      <path d="M322 13 C350 60 358 110 345 160 C330 205 318 240 324 276 L332 276 C326 240 336 205 350 160 C362 110 356 60 322 13 Z" fill="url(#shadowGray)"/>
      <path d="M322 13 C352 60 362 110 352 160 C340 205 328 240 334 276 L565 276 L565 13 Z" fill="#1f3f7f"/>
    </svg>
    <div class="brand">
      <span class="brand__square"></span><span class="brand__rule"></span>
      <p class="brand__name"><span class="brand__line1">HARLOW BROTHERS</span><span class="brand__line2">CIVIL CONSTRUCTION</span></p>
    </div>
    <ul class="services">
      <li>- CIVIL CONSTRUCTION SERVICES -</li><li>- LAND CLEARING -</li><li>- EXCAVATION -</li>
      <li>- UNDERGROUND UTILITIES -</li><li>- ENVIRONMENTAL MAINTENANCE -</li><li>- ROAD CONSTRUCTION -</li>
    </ul>
    <div class="hiring">
      <div class="hiring__mark"></div>
      <h2 class="hiring__title">NOW HIRING!</h2>
      <ul class="jobs"><li>SUPERINTENDENTS</li><li>PROJECT MANAGERS</li><li>PIPE FOREMEN</li><li>PIPE LAWYERS</li><li>EQUIPMENT OPERATORS</li></ul>
    </div>
  </section>

  <section class="sign sign--d">
    <svg class="sign__art" viewBox="0 0 578 289" aria-hidden="true">
      <defs>
        <linearGradient id="shadowLav" x1="0" y1="0" x2="0" y2="1">
          <stop offset="0" stop-color="#ffffff"/>
          <stop offset="0.45" stop-color="#7f83b8"/>
          <stop offset="1" stop-color="#ffffff"/>
        </linearGradient>
      </defs>
      <rect width="578" height="289" fill="#1f3f7f"/>
      <rect x="6" y="6" width="566" height="277" fill="#fff"/>
      <rect x="9" y="9" width="560" height="271" fill="#555659"/>
      <rect x="13" y="13" width="552" height="263" fill="#fff"/>
      <path d="M322 13 C350 60 358 110 345 160 C330 205 318 240 324 276 L332 276 C326 240 336 205 350 160 C362 110 356 60 322 13 Z" fill="url(#shadowLav)"/>
      <path d="M322 13 C352 60 362 110 352 160 C340 205 328 240 334 276 L565 276 L565 13 Z" fill="#1f3f7f"/>
    </svg>
    <div class="brand">
      <span class="brand__square"></span><span class="brand__rule"></span>
      <p class="brand__name"><span class="brand__line1">HARLOW BROTHERS</span><span class="brand__line2">CIVIL CONSTRUCTION</span></p>
    </div>
    <ul class="services">
      <li>- CIVIL CONSTRUCTION SERVICES -</li><li>- LAND CLEARING -</li><li>- EXCAVATION -</li>
      <li>- UNDERGROUND UTILITIES -</li><li>- ENVIRONMENTAL MAINTENANCE -</li><li>- ROAD CONSTRUCTION -</li>
    </ul>
    <div class="hiring">
      <div class="hiring__mark"></div>
      <h2 class="hiring__title">NOW HIRING!</h2>
      <ul class="jobs"><li>SUPERINTENDENTS</li><li>PROJECT MANAGERS</li><li>PIPE FOREMEN</li><li>PIPE LAWYERS</li><li>EQUIPMENT OPERATORS</li></ul>
    </div>
  </section>

</main>
</body>
</html>
```